Postcard - Promoting Wendell Ridge Brokers for Farm Clients

We need to develop a postcard (4" X 6") to send out to Agricultural clients.

The content on the email will be:

We understand that farming has variety of risk exposures that can affect your farm and your family’s future.
Wendell Ridge Brokers can help you identify and manage those risks by building an insurance program that works for you, your family and your operation. We ensure we understand your risk, you understand your coverage and we sort through the “fine” print together before a loss happens.
Contact Wendell Ridge Brokers to arrange a review and meet our team. 1-800-555-0147 farmteam@wendellridge.ca

Target Market(s)

We would like 2 separate postcards - one for crop farmers and one for cattle farmers

Industry/Entity Type

Agriculture

Requirements
Must have
• Be remarkable - something that catches your eye, and must have our logo

Please note that this can be 2 sided - potential to have the photo/color side to be the picture and some wording to catch the attention of the individual receiving .... and the back side to be the additional content, which is in the project description.

```html
<!DOCTYPE html>
<html lang="en">
<head>
<meta charset="utf-8">
<title>Wendell Ridge Brokers – Farm Postcard</title>
<link rel="stylesheet" href="https://fonts.googleapis.com/css2?family=Gelasio:wght@700&family=Arimo:wght@400&display=swap">
<style>
  :root {
    --page-bg: #e6e6e6;
    --card-bg: #f6f6f7;
    --navy: #1c2a5e;
    --royal: #1a50a6;
    --white: #ffffff;
    --ink: #1a1a1a;
    --sky: #bcd6ea;
    --grass: #6d9a3a;
    --hide: #7a3d18;
  }
  * { box-sizing: border-box; margin: 0; padding: 0; }
  html, body {
    width: 970px; height: 1200px; overflow: hidden;
    background: var(--page-bg);
  }
  .postcard {
    position: absolute; left: 145px; width: 685px; height: 456px;
    background: var(--card-bg); overflow: hidden;
  }
  .postcard--front { top: 125px; }
  .postcard--back { top: 616px; height: 450px; }
  .front-art { display: block; width: 100%; height: 100%; }
  .brand-name {
    font-family: "Gelasio", Georgia, serif; font-weight: 700;
    fill: var(--navy);
  }

  .message-panel {
    position: absolute; left: 0; top: 0; width: 330px; height: 100%;
    background: var(--navy); color: var(--white);
    padding: 35px 28px 0 35px;
  }
  .message-panel__headline {
    font-family: "Gelasio", Georgia, serif; font-weight: 700;
    font-size: 17.5px; line-height: 22px;
  }
  .message-panel__body {
    font-family: "Arimo", Arial, sans-serif; font-size: 11.6px;
    line-height: 15.1px; margin-top: 18px;
  }
  .message-panel__rule {
    width: 58px; height: 2px; background: var(--white);
    margin-top: 30px; margin-left: 1px;
  }
  .message-panel__cta {
    font-family: "Gelasio", Georgia, serif; font-weight: 700;
    font-size: 17.5px; line-height: 21px; margin-top: 27px;
  }
  .message-panel__contact {
    font-family: "Arimo", Arial, sans-serif; font-size: 14.5px;
    line-height: 19px; margin-top: 10px; margin-left: 1px;
  }

  .stamp-box {
    position: absolute; left: 548px; top: 37px; width: 95px; height: 117px;
    border: 1.2px solid var(--ink);
  }
  .address-line {
    position: absolute; left: 388px; width: 254px; height: 1.2px;
    background: var(--ink);
  }
  .address-line--1 { top: 243px; }
  .address-line--2 { top: 283px; }
  .address-line--3 { top: 322px; }
</style>
</head>
<body>

<section class="postcard postcard--front">
  <svg class="front-art" viewBox="0 0 1142 760" xmlns="http://www.w3.org/2000/svg">
    <defs>
      <linearGradient id="sky-field" x1="0" y1="0" x2="0.6" y2="1">
        <stop offset="0" stop-color="#c9deee"/>
        <stop offset="0.55" stop-color="#9cbfd8"/>
        <stop offset="1" stop-color="#7a4a24"/>
      </linearGradient>
      <linearGradient id="calf-field" x1="0.2" y1="0" x2="0.8" y2="1">
        <stop offset="0" stop-color="#a9c9df"/>
        <stop offset="0.3" stop-color="#8a4a1e"/>
        <stop offset="0.65" stop-color="#6b3314"/>
        <stop offset="1" stop-color="#4a230e"/>
      </linearGradient>
    </defs>

    <polygon class="photo-area" role="img" aria-label="Photo: sky and pasture behind a young brown calf"
      points="0,0 576,0 238,338 0,107" fill="url(#sky-field)"/>
    <polygon class="accent-triangle" points="0,157 208,364 0,572" fill="var(--royal)"/>
    <polygon class="photo-area" role="img" aria-label="Photo: close-up of a shaggy brown calf standing in a green pasture"
      points="603,22 945,364 548,760 0,760 0,622" fill="url(#calf-field)"/>
    <polygon class="accent-block" points="636,0 1142,0 1142,170 971,337" fill="var(--navy)"/>

    <g class="brand">
      <circle cx="923" cy="775" r="0" fill="none"/>
      <circle cx="923" cy="562" r="40" fill="var(--navy)"/>
      <text class="brand-name" x="923" y="665" text-anchor="middle" font-size="38">WENDELL RIDGE</text>
      <text class="brand-name" x="923" y="710" text-anchor="middle" font-size="38">BROKERS</text>
    </g>
  </svg>
</section>

<section class="postcard postcard--back">
  <div class="message-panel">
    <h1 class="message-panel__headline">We understand that farming has variety of risk exposures that can affect your farm and your family’s future.</h1>
    <p class="message-panel__body">Wendell Ridge Brokers can help you identify and manage those risks by building an insurance program that works for you, your family and your operation. We ensure we understand your risk, you understand your coverage and we sort through the “fine” print together before a loss happens.</p>
    <div class="message-panel__rule"></div>
    <h2 class="message-panel__cta">Contact Wendell Ridge Brokers to arrange a review and meet our team.</h2>
    <p class="message-panel__contact">1-800-555-0147<br>farmteam@wendellridge.ca</p>
  </div>
  <div class="stamp-box"></div>
  <div class="address-line address-line--1"></div>
  <div class="address-line address-line--2"></div>
  <div class="address-line address-line--3"></div>
</section>

</body>
</html>
```